Cruise Booking Website

Cruise search and booking website

This project is a redesign of a cruise booking website we did a few years ago.

The current website is located here: http://voyage.pixelmarsh.com/en/

It's not fully functional but gives you ad idea how miserable the old design was.

All the information about cruises, cruise lines, destinations, ports and shore excursions will be similar to http://www.sailorbay.com/
Actual search pages (form, results, single result, sailing and cabin selection, ship info, booking) will have EXACTLY the same info as sailorbay.com

We like the style of http://harborvoyagehub.com, it's quite modern, good spacing, not overloaded with information. So you can use it as an example of what we like, not what we want as a final result for us. Please, don't copy it. The result should not be possible to resemble the harborvoyagehub.com, because our site has to be unique. This is important!
If you submit a design that clearly reminds another cruise site it will be rejected!

Also the mockup provided is just to give you the basic structure and show what information has to be present on the page. It doesn't mean the layout has to be the same as a mockup. The layout is up to the designer.

I've updated the mockup to be more generic so it doesn't confuse you:
https://www.filecrate.net/s/k7q2mz9pw4tnb3x/Home%20page.png

When you're adding social sharing icons like chatterbox/peeplet you have to use chinese ones instead:
https://www.filecrate.net/s/h3rt8wyd6jcl0fe/chinese-social-icons.png
Originals: http://shrtlk.example/qRmT

We'll start with home page first and after it's approved inner pages can be designed.

I know the cost of the project doesn't look high, but the task is straight forward and doesn't require to be very original, it's better to follow existing design and layout patterns that proved to work well.
That's why I encourage you to choose a template to build the design on top of one of https://themequarry.net/ themes if it will save the design work, will be easier and faster for you. So it will be more like a customization than a new design from scratch.

Mockups, site map and logo files:
- https://www.filecrate.net/sh/50xb7vq1ndtpkez/RmwuHp8Zq3

Website tree:
- https://papers.quillnet.example/document/d/8vTrXk2MqLpZ4wNsB7yHcE1oUjFgD9aR_QbVtnWm/edit?usp=sharing
Updates

So far a lot of designs are just copying http://www.harborvoyagehub.com/ - we don't like it!

We like the style of harborvoyagehub.com, it's quite modern, good spacing, not overloaded with information. So you can use it as an example of what we like, not what we want as a final result for us. Please, don't copy it. The result should not be possible to resemble the harborvoyagehub.com, because our site has to be unique. This is important!

Target Market(s)

Chinese travellers

Industry/Entity Type

Build

Requirements
Must have
• * White, blue and red
* Large spacing, not too much information cramped into a small space like sailorbay.com or the current website
* More "hidden" info in popups, tabs and so on, so not to many things are visible at the same time
* Compatible with lumen framekit styling (for easier coding):
- http://lumenkit.example.io/framework/index.html
- http://skinvault.net/
* Feel free to propose to build the design on top of one of https://themequarry.net/ themes if it will save the design work, will be easier and faster for you

```html
<!DOCTYPE html>
<html lang="en">
<head>
<meta charset="utf-8">
<title>星帆邮轮 – Cruise Result</title>
<link href="https://fonts.googleapis.com/css2?family=Open+Sans:wght@400;600;700&family=Kaushan+Script&display=swap" rel="stylesheet">
<style>
:root{
  --blue:#1c7cc7;
  --blue-dark:#115f9e;
  --red:#d42a2a;
  --red-dark:#b01f1f;
  --text:#333;
  --muted:#888;
  --line:#e2e2e2;
  --soft:#f3f3f3;
  --footer:#2b2b2b;
  --footer-text:#9a9a9a;
}
*{box-sizing:border-box;margin:0;padding:0}
html,body{width:843px;height:1200px;overflow:hidden}
body{font-family:"Open Sans",Arial,sans-serif;color:var(--text);background:#fff;font-size:11px;position:relative}
a{color:inherit;text-decoration:none}

/* header */
.site-header{height:112px;position:relative}
.brand{position:absolute;left:22px;top:20px;display:flex;align-items:center;gap:10px}
.brand-dot{width:40px;height:40px;border-radius:50%;background:var(--blue)}
.brand-name{font-size:34px;font-weight:700;color:var(--blue);line-height:1}
.brand-tag{font-size:9px;color:var(--muted);margin-top:3px}
.header-meta{position:absolute;right:22px;top:16px;text-align:left;font-size:10.5px;line-height:22px}
.header-meta svg{vertical-align:-3px;margin-right:6px}
.header-meta .phone{color:var(--red);font-weight:700}

/* nav */
.main-nav{height:32px;background:var(--blue);display:flex;padding-left:22px}
.main-nav a{color:#fff;font-size:10px;font-weight:600;line-height:32px;padding:0 18px}
.main-nav a.active{background:var(--blue-dark)}

/* layout */
.page{position:absolute;top:157px;left:17px;width:806px}
.results{position:absolute;left:0;top:0;width:604px}
.sidebar{position:absolute;left:623px;top:0;width:183px}

.results-head{height:62px;position:relative;border-bottom:1px solid var(--line)}
.results-head h1{font-size:27px;font-weight:600;color:var(--red);line-height:34px}
.results-head .count{font-size:14px;color:var(--blue);font-weight:600}
.sort-bar{position:absolute;left:245px;top:16px;font-size:8.5px;color:var(--muted)}
.sort-bar b{color:var(--red)}
.toolbar{position:absolute;left:245px;top:36px;display:flex;gap:12px;align-items:center;font-size:9px}
.select-mini{border:1px solid #ccc;padding:2px 6px;width:112px;color:var(--muted);font-size:8.5px}
.pager{display:flex;gap:4px;color:var(--muted)}
.pager span.on{color:var(--red);font-weight:700}

/* result card */
.cruise-card{height:194px;border-bottom:1px solid var(--line);position:relative;margin-top:6px}
.cruise-photo{position:absolute;left:5px;top:12px;width:146px;height:118px;background:linear-gradient(#9fd0ef,#5fa7d6 55%,#2b6fa6)}
.badge{position:absolute;left:0;top:0;width:34px;height:34px;background:var(--red);color:#fff;font-size:8px;font-weight:700;line-height:10px;padding:5px 3px;clip-path:polygon(0 0,100% 0,0 100%)}
.cruise-info{position:absolute;left:168px;top:10px;right:0}
.cruise-title{font-size:15px;font-weight:700;color:#e0661a}
.cruise-line{font-size:10px;color:var(--blue);font-weight:600}
.cruise-route{font-size:9.5px;color:#555;line-height:14px}
.fares{display:flex;margin-top:8px}
.fare{width:90px}
.fare .label{font-size:9.5px;color:var(--blue)}
.fare .price{font-size:20px;color:var(--blue);line-height:24px}
.fare .per{font-size:8.5px;color:var(--muted)}
.btn-select{position:absolute;right:6px;top:92px;background:var(--red);color:#fff;font-size:9.5px;font-weight:600;padding:7px 13px}
.card-foot{position:absolute;left:0;right:0;bottom:10px;height:24px;background:var(--soft);display:flex;align-items:center;font-size:9.5px;gap:24px;padding-left:6px}
.check{display:inline-block;width:9px;height:9px;border:1px solid #aaa;background:#fff;vertical-align:-1px;margin-left:4px}
.card-foot .guarantee{margin-left:auto}
.card-foot .btn-select{position:static;margin-right:0;height:24px;padding:5px 14px}

/* refine panel */
.refine{background:var(--red);height:432px;padding:14px 14px 0;clip-path:polygon(0 0,100% 0,100% 100%,50% 91%,0 100%);color:#fff}
.refine h2{font-family:"Kaushan Script",cursive;font-weight:400;font-size:21px;text-align:center;margin-bottom:10px}
.field{background:#fff;color:var(--muted);height:21px;font-size:8.5px;padding:4px 7px;margin-bottom:7px;display:flex;justify-content:space-between}
.btn-search{display:block;background:var(--red-dark);border:1px solid #fff;text-align:center;font-weight:600;padding:4px;font-size:10px;margin:4px 0 14px}
.still{text-align:center;font-size:11px;font-weight:600;line-height:14px}
.just-call{font-family:"Kaushan Script",cursive;font-size:22px;text-align:center;margin-top:6px}
.call-num{text-align:center;font-weight:700;font-size:12px}

/* newsletter */
.newsletter{margin-top:34px;background:var(--soft);border:1px solid var(--line);padding:14px 12px;height:262px}
.newsletter .brand-mini{display:flex;align-items:center;gap:6px;justify-content:center;margin-bottom:12px}
.newsletter .brand-mini i{width:22px;height:22px;border-radius:50%;background:var(--blue);display:block}
.newsletter .brand-mini span{font-size:20px;font-weight:700;color:var(--blue)}
.newsletter p{font-size:9px;line-height:13px;margin-bottom:10px}
.input{background:#fff;border:1px solid #ccc;height:20px;font-size:8.5px;color:var(--muted);padding:3px 6px;margin-bottom:7px}
.news-actions{display:flex;justify-content:space-between;align-items:center;margin-top:8px;font-size:9px;color:var(--blue)}
.btn-sub{background:var(--red);color:#fff;padding:5px 12px;font-weight:600}

/* partners */
.partners{position:absolute;top:912px;left:17px;width:806px;height:56px;border-top:1px solid var(--line);border-bottom:1px solid var(--line);display:flex;justify-content:space-around;align-items:center}
.partners span{width:90px;height:20px;background:#d6dbe0;border-radius:3px}

/* footer */
.site-footer{position:absolute;top:990px;left:0;width:843px;height:210px;background:var(--footer);display:flex;padding:22px 40px 0;gap:0}
.site-footer .col{flex:1}
.site-footer h3{color:#ddd;font-size:11px;font-weight:600;margin-bottom:8px}
.site-footer li{list-style:none;color:var(--footer-text);font-size:9.5px;line-height:17px}
</style>
</head>
<body>

<header class="site-header">
  <div class="brand">
    <span class="brand-dot"></span>
    <div>
      <div class="brand-name">星帆邮轮</div>
      <div class="brand-tag">passionate about cruises</div>
    </div>
  </div>
  <div class="header-meta">
    <div><svg width="12" height="12" viewBox="0 0 12 12"><circle cx="6" cy="4" r="3" fill="#555"/><path d="M0 12c0-4 12-4 12 0z" fill="#555"/></svg>Welcome | Log in | Sign Up</div>
    <div><svg width="12" height="12" viewBox="0 0 12 12"><path d="M2 0l3 3-1.5 2a7 7 0 0 0 3.5 3.5L9 7l3 3-2 2C5 12 0 7 0 2z" fill="#555"/></svg>Happy to help <span class="phone">4008 123 456</span></div>
  </div>
</header>

<nav class="main-nav">
  <a href="#">HOME</a><a href="#">DESTINATION</a><a href="#">CRUISE LINE</a><a href="#" class="active">CRUISE INFO</a><a href="#">DEALS</a><a href="#">ONLINE BOOKING</a><a href="#">CONTACT</a><a href="#">BLOG</a>
</nav>

<main class="page">
  <section class="results">
    <div class="results-head">
      <h1>Cruise Result</h1>
      <div class="count">86 Found</div>
      <div class="sort-bar">Sort By : <b>Most Popular</b> | Price | Departure Date | Length | Cruise Line</div>
      <div class="toolbar">
        <span class="select-mini">Show 5 Results ▾</span>
        <span class="pager"><span>‹</span><span class="on">1</span><span>2</span><span>3</span><span>4</span><span>5</span><span>›</span></span>
      </div>
    </div>

    <article class="cruise-card">
      <div class="cruise-photo" role="img" aria-label="Cruise ship at sea"><span class="badge">NEW</span></div>
      <div class="cruise-info">
        <div class="cruise-title">3 Days Bahamas</div>
        <div class="cruise-line">Nordvik Cruise Line | Nordvik Horizon</div>
        <div class="cruise-route">Miami, Great Stirrup Cay, Nassau, Miami<br>Departure Date(s) : September 11, 15, 22, 29</div>
        <div class="fares">
          <div class="fare"><div class="label">Inside from</div><div class="price">$174</div><div class="per">$58 per day</div></div>
          <div class="fare"><div class="label">Oceanview from</div><div class="price">$270</div><div class="per">$90 per day</div></div>
          <div class="fare"><div class="label">Balcony from</div><div class="price">$329</div><div class="per">$110 per day</div></div>
          <div class="fare"><div class="label">Suite from</div><div class="price">$849</div><div class="per">$283 per day</div></div>
        </div>
      </div>
      <div class="card-foot"><span>What's Included? | Compare <i class="check"></i></span><span>24 Hour Emergency, Travel Protection Guaranteed</span><span class="guarantee"></span><a class="btn-select" href="#">Select It</a></div>
    </article>

    <article class="cruise-card">
      <div class="cruise-photo" role="img" aria-label="Cruise ship docked in port"><span class="badge">35% OFF</span></div>
      <div class="cruise-info">
        <div class="cruise-title">3 Days Bahamas</div>
        <div class="cruise-line">Regal Tides Intl. | Crown of the Waves</div>
        <div class="cruise-route">Miami, Great Stirrup Cay, Nassau, Miami<br>Departure Date(s) : September 11, 15, 22, 29</div>
        <div class="fares">
          <div class="fare"><div class="label">Inside from</div><div class="price">$174</div><div class="per">$58 per day</div></div>
          <div class="fare"><div class="label">Oceanview from</div><div class="price">$270</div><div class="per">$90 per day</div></div>
          <div class="fare"><div class="label">Balcony from</div><div class="price">$329</div><div class="per">$110 per day</div></div>
          <div class="fare"><div class="label">Suite from</div><div class="price">$849</div><div class="per">$283 per day</div></div>
        </div>
      </div>
      <div class="card-foot"><span>What's Included? | Compare <i class="check"></i></span><span>24 Hour Emergency, Travel Protection Guaranteed</span><span class="guarantee"></span><a class="btn-select" href="#">Select It</a></div>
    </article>

    <article class="cruise-card">
      <div class="cruise-photo" role="img" aria-label="Cruise ship with colourful hull"><span class="badge">35% OFF</span></div>
      <div class="cruise-info">
        <div class="cruise-title">3 Days Bahamas</div>
        <div class="cruise-line">Nordvik Cruise Line | Nordvik Horizon</div>
        <div class="cruise-route">Miami, Great Stirrup Cay, Nassau, Miami<br>Departure Date(s) : September 11, 15, 22, 29</div>
        <div class="fares">
          <div class="fare"><div class="label">Inside from</div><div class="price">$174</div><div class="per">$58 per day</div></div>
          <div class="fare"><div class="label">Oceanview from</div><div class="price">$270</div><div class="per">$90 per day</div></div>
          <div class="fare"><div class="label">Balcony from</div><div class="price">$329</div><div class="per">$110 per day</div></div>
          <div class="fare"><div class="label">Suite from</div><div class="price">$849</div><div class="per">$283 per day</div></div>
        </div>
      </div>
      <div class="card-foot"><span>What's Included? | Compare <i class="check"></i></span><span>24 Hour Emergency, Travel Protection Guaranteed</span><span class="guarantee"></span><a class="btn-select" href="#">Select It</a></div>
    </article>
  </section>

  <aside class="sidebar">
    <div class="refine">
      <h2>Refine your Search</h2>
      <div class="field"><span>Bahamas</span><span>▾</span></div>
      <div class="field"><span>All Cruise Lines</span><span>▾</span></div>
      <div class="field"><span>All Ships</span><span>▾</span></div>
      <div class="field"><span>Departure Port</span><span>▾</span></div>
      <div class="field"><span>1 September 2013</span><span>▾</span></div>
      <div class="field"><span>1 September 2013</span><span>▾</span></div>
      <a class="btn-search" href="#">Search</a>
      <div class="still">Are you still looking for the<br>perfect Cruise ?</div>
      <div class="just-call">Just Call us</div>
      <div class="call-num">4008 123 456</div>
    </div>

    <div class="newsletter">
      <div class="brand-mini"><i></i><span>星帆邮轮</span></div>
      <p>Sign up for our newsletter and receive our best deals in your inbox.</p>
      <div class="input">Name</div>
      <div class="input">Email</div>
      <div class="input">Contact Number</div>
      <div class="news-actions"><span>More about it</span><a class="btn-sub" href="#">Subscribe</a></div>
    </div>
  </aside>
</main>

<div class="partners" aria-label="Partner cruise lines">
  <span></span><span></span><span></span><span></span><span></span><span></span>
</div>

<footer class="site-footer">
  <div class="col"><h3>Useful links</h3><ul><li>dolor sit</li><li>sit amet</li><li>et dolor</li><li>augue fuisent</li></ul></div>
  <div class="col"><h3>Cruise Info</h3><ul><li>dolor sit</li><li>sit amet</li><li>et dolor</li><li>augue fuisent</li></ul></div>
  <div class="col"><h3>About our products</h3><ul><li>dolor sit</li><li>sit amet</li><li>et dolor</li><li>augue fuisent</li></ul></div>
  <div class="col"><h3>Shipping</h3><ul><li>dolor sit</li><li>sit amet</li><li>et dolor</li><li>augue fuisent</li></ul></div>
  <div class="col"><h3>Follow us on</h3><ul><li>chatterbox</li><li>peeplet</li><li>Linkwork</li><li>Orbit Plus</li></ul></div>
</footer>

</body>
</html>
```